drink bottle label

Our drink is called VELTRANA qa, a 2000 year old Asian formula for a fermented green tea drink. Flavored with organic ginger juice, cinnamon and lime. Very tasty and refreshing, good for sports recovery, digestion,liver detox,overall health and vitality. Naturally fermented creating a- no sugar, low GI, salt,-fat and gluten free- fizzy drink alternative to soft drink, sports drinks or beer. The bottle is a brown 330ml long neck bottle. For the diet and health conscious individual. We would like the label to be upmarket for restaurants & trendy organic food suppliers.
Updates

The bottle is brown. Try using black-gold-silver-white for the subject in a white or silver border

Target Market(s)

Upmarket, for restaurant & trendy organic food supplies.Sophisticated Health conscious people who don't want high sugar, caffeine drinks.

Industry/Entity Type

Health

Requirements
Must have
• The drink name and registered brand is" VELTRANA qa."
Must feature PROBIOTICS & ENZYMES for detox.No artificial preservatives or colours. 100% Organic & raw living culture.Low GI low calorie- no cane sugar, no salt-
- no lactose, Coeliac -diabetic & vegan friendly. Ginger Brew.
Nice to have
• tastes great-revitalize- 330ml brown bottle

```html
<!DOCTYPE html>
<html lang="en">
<head>
<meta charset="utf-8">
<title>VELTRANA qa – bottle labels</title>
<link rel="stylesheet" href="https://fonts.googleapis.com/css2?family=Arimo:wght@400;700&display=swap">
<style>
  :root{
    --gold:#DA9E2B;
    --black:#0d0d0d;
    --pattern:#2b2b2b;
    --silver-light:#f2f2f2;
    --silver-mid:#bdbdbd;
    --silver-dark:#8a8a8a;
    --white:#ffffff;
  }
  *{margin:0;padding:0;box-sizing:border-box}
  html,body{width:1200px;height:1071px;overflow:hidden;background:var(--white)}
  body{font-family:"Arimo",Arial,sans-serif;position:relative}
  .gold-band{position:absolute;left:0;top:0;width:224px;height:1071px;background:var(--gold)}
  .shapes{position:absolute;left:0;top:0}
  .t{position:absolute;color:var(--white);font-weight:700;line-height:1}
  .brand-title{left:262px;top:966px;color:var(--gold);font-size:36px;letter-spacing:.5px}
  .brand-title small,.front-name small{font-size:.75em}
  .front-tagline{right:360px;top:579px;font-size:6px}
  .front-name{right:360px;top:594px;font-size:22px;letter-spacing:.5px}
  .front-sub{left:603px;width:249px;text-align:center;top:627px;font-size:13px}
  .front-flavours{left:603px;width:249px;text-align:center;top:647px;font-size:12px;color:var(--gold)}
  .claims{left:603px;width:249px;text-align:center;font-size:10px;line-height:14px;top:855px}
  .claims .first{font-size:8px}
  .volume{left:603px;width:249px;text-align:center;top:906px;font-size:8px}
  .copy{font-size:8.4px;line-height:10px;font-weight:700;color:var(--white);position:absolute}
  .copy-left{left:365px;top:508px;width:170px}
  .copy-right{left:916px;top:521px;width:140px}
  .nut-title{font-size:9.5px}
  .nut-title-left{left:343px;top:667px}
  .nut-title-right{left:911px;top:671px;font-size:10.5px}
  .nut-amount{font-size:4px}
  .nut-amount-left{left:343px;top:684px}
  .nut-amount-right{left:911px;top:689px}
  .ingredients{font-size:6px;font-weight:400}
  .ingredients-left{left:430px;top:660px}
  .ingredients-right{left:1017px;top:675px}
</style>
</head>
<body>
<div class="gold-band"></div>

<svg class="shapes" width="1200" height="1071" viewBox="0 0 1200 1071">
  <defs>
    <linearGradient id="silver" x1="0" y1="0" x2="1" y2="0">
      <stop offset="0" stop-color="#9a9a9a"/>
      <stop offset=".35" stop-color="#f4f4f4"/>
      <stop offset=".7" stop-color="#c4c4c4"/>
      <stop offset="1" stop-color="#8d8d8d"/>
    </linearGradient>
    <radialGradient id="produce" cx=".5" cy=".5" r=".5">
      <stop offset="0" stop-color="#f3c24d"/>
      <stop offset=".55" stop-color="#7fb33a"/>
      <stop offset="1" stop-color="#0d0d0d" stop-opacity="0"/>
    </radialGradient>
  </defs>

  <!-- left back label -->
  <g class="label label-left">
    <path d="M323,500 C323,455 350,421 434,420 C518,421 545,455 545,500 L545,832 L323,832 Z" fill="url(#silver)"/>
    <path d="M323,508 C330,470 356,436 434,435 C512,436 538,470 545,508 L545,815 L323,815 Z" fill="var(--black)"/>
    <rect x="323" y="655" width="222" height="160" fill="var(--pattern)" role="img" aria-label="Dark star lattice pattern"/>
    <circle cx="388" cy="488" r="16" fill="var(--silver-mid)" stroke="var(--white)" stroke-width="1.5"/>
    <circle cx="432" cy="488" r="16" fill="var(--silver-mid)" stroke="var(--white)" stroke-width="1.5"/>
    <circle cx="480" cy="488" r="16" fill="var(--silver-mid)" stroke="var(--white)" stroke-width="1.5"/>
    <rect x="340" y="663" width="80" height="128" fill="none" stroke="var(--white)" stroke-width="2"/>
    <line x1="340" y1="680" x2="420" y2="680" stroke="var(--white)" stroke-width="2"/>
    <line x1="340" y1="696" x2="420" y2="696" stroke="var(--white)" stroke-width="1"/>
    <line x1="344" y1="755" x2="416" y2="755" stroke="var(--white)" stroke-width="1.5"/>
  </g>

  <!-- front label -->
  <g class="label label-front">
    <path d="M603,575 C603,528 628,499 727,497 C826,499 852,528 852,575 L852,950 L603,950 Z" fill="url(#silver)"/>
    <path d="M603,582 C612,540 638,512 727,510 C816,512 843,540 852,582 L852,930 L603,930 Z" fill="var(--black)"/>
    <rect x="603" y="755" width="249" height="150" fill="var(--pattern)" role="img" aria-label="Dark star lattice pattern"/>
    <rect x="655" y="690" width="150" height="150" fill="url(#produce)" role="img" aria-label="Illustration of halved limes, ginger slices and cinnamon sticks"/>
    <line x1="622" y1="897" x2="833" y2="897" stroke="var(--silver-dark)" stroke-width=".6"/>
  </g>

  <!-- right back label -->
  <g class="label label-right">
    <path d="M895,510 C895,465 925,431 1015,430 C1106,431 1136,465 1136,510 L1136,845 L895,845 Z" fill="url(#silver)"/>
    <path d="M895,518 C902,480 930,446 1015,445 C1100,446 1129,480 1136,518 L1136,830 L895,830 Z" fill="var(--black)"/>
    <rect x="895" y="668" width="241" height="162" fill="var(--pattern)" role="img" aria-label="Dark star lattice pattern"/>
    <circle cx="1073" cy="533" r="17" fill="var(--silver-mid)" stroke="var(--white)" stroke-width="1.5"/>
    <circle cx="1073" cy="588" r="17" fill="var(--silver-mid)" stroke="var(--white)" stroke-width="1.5"/>
    <circle cx="1073" cy="638" r="17" fill="var(--silver-mid)" stroke="var(--white)" stroke-width="1.5"/>
    <rect x="908" y="667" width="100" height="138" fill="none" stroke="var(--white)" stroke-width="2"/>
    <line x1="908" y1="685" x2="1008" y2="685" stroke="var(--white)" stroke-width="2"/>
    <line x1="908" y1="700" x2="1008" y2="700" stroke="var(--white)" stroke-width="1"/>
    <line x1="912" y1="776" x2="1004" y2="776" stroke="var(--white)" stroke-width="1.5"/>
  </g>
</svg>

<div class="t front-tagline">100% Organic &amp; raw living culture by Culterra pty.ltd.</div>
<div class="t front-name">VELTRANA <small>qa</small></div>
<div class="t front-sub">Organic Naturally Fermemted Tea</div>
<div class="t front-flavours">with Lime • Cinnamon • Ginger Juice</div>
<div class="t claims">
  <div class="first">No cane sugar • No gluten • No lactose</div>
  <div>No glucose • No salt • Low calorie • Low GI</div>
  <div>Coeliac • Diabetic • Vegan</div>
</div>
<div class="t volume">330ml</div>

<p class="copy copy-left">Lorem ipsum dolor sit amet, consectetur adipiscing elit. Vestibulum eu elit erat. Maecenas rhoncus dui sed interdum tincidunt. Aliquam arcu turpis, dapibus quis orci eu, sodales laoreet elit. Proin nec auctor enim. Class aptent taciti sociosqu ad litora torquent per conubia nostra, per inceptos himenaeos. Cras arcu mi, ultricies ullamcorper massa eget, lacinia vulputate arcu. Quisque eget pretium lorem, ac fringilla sem.</p>
<p class="copy copy-right">Lorem ipsum dolor sit amet, consectetur adipiscing elit. Vestibulum eu elit erat. Maecenas rhoncus dui sed interdum tincidunt. Aliquam arcu turpis, dapibus quis orci eu, sodales laoreet elit. Proin nec auctor enim. Class aptent taciti sociosqu ad litora torquent per conubia nostra, per inceptos himenaeos. Cras arcu mi, ultricies ullamcorper massa eget, lacinia vulputate arcu. Quisque eget pretium lorem, ac fringilla sem.</p>

<div class="t nut-title nut-title-left">Nutrition Facts</div>
<div class="t nut-amount nut-amount-left">Amount Per serving</div>
<div class="t ingredients ingredients-left">INGREDIENTS:</div>
<div class="t nut-title nut-title-right">Nutrition Facts</div>
<div class="t nut-amount nut-amount-right">Amount Per serving</div>
<div class="t ingredients ingredients-right">INGREDIENTS:</div>

<div class="t brand-title">VELTRANA <small>qa</small></div>
</body>
</html>
```